Appointments cards for my business "Bluebell slimming clinic"

I need an appointment card for my business, I will attach the current business card, the logo its self will stay the same, I will attach my most recent personal business card as well. Im looking for a cross in-between both cards not to fancy though.
the back of the card will have the appointment date and time on it... But I don't want my photo on these appointment cards. thank you

Target Market(s)

25-50 year old

Industry/Entity Type

Health Care

Contact Information for Business Card

Bluebell Slimming & Balance clinic
1746 brook st ste#2
riverton hills co 80512
phone# (555) 214-7720
fax# (555)214-7721
bluebellslimclinic.com

Font styles to use
Serif
Sans Serif
Script

Colors

Designer to choose colors to be used in the design.

Requirements
Must have
• the logo the address ...info
Nice to have
• I would like to mix my new card with logo and my business card
Should not have
• see above

```html
<!DOCTYPE html>
<html lang="en">
<head>
<meta charset="utf-8">
<title>Bluebell slimming clinic – appointment card</title>
<link rel="stylesheet" href="https://fonts.googleapis.com/css2?family=Tinos&family=Work+Sans:wght@400;500&display=swap">
<style>
  :root {
    --backdrop: #dedede;
    --card: #ffffff;
    --ink: #1e1a18;
    --gold: #c79a2c;
    --gold-line: #c9a040;
    --shadow: rgba(0, 0, 0, 0.22);
  }
  * { box-sizing: border-box; margin: 0; padding: 0; }
  html, body { width: 1200px; height: 859px; overflow: hidden; }
  body {
    background: var(--backdrop);
    position: relative;
    font-family: "Work Sans", Arial, sans-serif;
    color: var(--ink);
  }
  .card {
    position: absolute;
    width: 560px;
    height: 320px;
    background: var(--card);
    border-radius: 18px;
    box-shadow: 0 6px 14px var(--shadow);
  }
  .card--appointment { left: 150px; top: 80px; }
  .card--contact { left: 490px; top: 460px; }

  /* appointment side */
  .appointment__title {
    position: absolute; left: 0; right: 0; top: 58px;
    text-align: center;
    font-family: "Tinos", "Times New Roman", serif;
    font-weight: 400;
    font-size: 24px; letter-spacing: 0.5px;
    text-transform: uppercase;
  }
  .appointment__heading {
    position: absolute; left: 0; right: 0; top: 126px;
    text-align: center;
    font-family: "Tinos", "Times New Roman", serif;
    font-weight: 400;
    font-size: 17px; color: var(--gold);
    text-transform: uppercase; letter-spacing: 0.5px;
  }
  .appointment__rule {
    position: absolute; left: 330px; right: 100px; top: 160px;
    border-top: 1px solid var(--gold-line);
  }
  .field {
    position: absolute; left: 70px; right: 60px;
    display: flex; align-items: flex-end; gap: 8px;
    font-family: "Tinos", "Times New Roman", serif;
    font-size: 16px; color: var(--gold);
  }
  .field--date { top: 196px; }
  .field--time { top: 248px; left: 92px; }
  .field__line { flex: 1; border-bottom: 1px solid var(--gold-line); height: 1px; margin-bottom: 4px; }

  /* contact side */
  .brand {
    position: absolute; left: 60px; top: 46px;
    display: flex; align-items: center; gap: 12px;
  }
  .brand__dot { width: 22px; height: 22px; border-radius: 50%; background: var(--gold); }
  .brand__name {
    font-family: "Tinos", "Times New Roman", serif;
    font-size: 22px; color: var(--gold);
    text-transform: uppercase; letter-spacing: 1px;
  }
  .person {
    position: absolute; right: 50px; top: 110px; text-align: right;
  }
  .person__name {
    font-family: "Tinos", "Times New Roman", serif;
    font-size: 32px; color: var(--gold); line-height: 1;
  }
  .person__role { font-size: 15px; margin-top: 2px; }
  .contact__rule {
    position: absolute; left: 40px; right: 50px; top: 186px;
    border-top: 2px solid var(--gold-line);
  }
  .address {
    position: absolute; right: 50px; top: 202px;
    text-align: right; font-size: 15px; line-height: 1.35;
    font-style: normal;
  }
  .contact-list {
    position: absolute; left: 40px; bottom: 18px;
    list-style: none; font-size: 17px; line-height: 1.35;
  }
  .contact-list li { display: flex; align-items: center; gap: 10px; }
  .contact-list svg { width: 13px; height: 13px; fill: var(--gold); flex: none; }
</style>
</head>
<body>

<section class="card card--appointment">
  <h1 class="appointment__title">Bluebell Slimming &amp; Balance clinic</h1>
  <h2 class="appointment__heading">Your next appointment</h2>
  <div class="appointment__rule"></div>
  <div class="field field--date"><span>Date :</span><span class="field__line"></span></div>
  <div class="field field--time"><span>Time :</span><span class="field__line"></span></div>
</section>

<section class="card card--contact">
  <div class="brand">
    <span class="brand__dot"></span>
    <span class="brand__name">Bluebell slimming clinic</span>
  </div>
  <div class="person">
    <div class="person__name">Marla Jensen</div>
    <div class="person__role">Director</div>
  </div>
  <div class="contact__rule"></div>
  <address class="address">
    1746 brook st ste#2<br>riverton hills co 80512
  </address>
  <ul class="contact-list">
    <li>
      <svg viewBox="0 0 24 24" aria-hidden="true"><path d="M6.6 10.8a15 15 0 0 0 6.6 6.6l2.2-2.2a1 1 0 0 1 1-.25 11.4 11.4 0 0 0 3.6.6 1 1 0 0 1 1 1V20a1 1 0 0 1-1 1A17 17 0 0 1 3 4a1 1 0 0 1 1-1h3.5a1 1 0 0 1 1 1c0 1.25.2 2.45.6 3.6a1 1 0 0 1-.25 1z"/></svg>
      (555) 214-7720
    </li>
    <li>
      <svg viewBox="0 0 24 24" aria-hidden="true"><path d="M6 3h10v5H6zM3 9h18v9h-3v3H6v-3H3zm5 6v4h8v-4z"/></svg>
      (555)214-7721
    </li>
    <li>
      <svg viewBox="0 0 24 24" aria-hidden="true"><path d="M12 2a10 10 0 1 0 0 20 10 10 0 0 0 0-20zm0 2c.9 0 2.2 2 2.7 5H9.3C9.8 6 11.1 4 12 4zM4.3 11h4.8a18 18 0 0 0 0 2H4.3a8 8 0 0 1 0-2zm10.6 0h4.8a8 8 0 0 1 0 2h-4.8a18 18 0 0 0 0-2zM9.3 15h5.4c-.5 3-1.8 5-2.7 5s-2.2-2-2.7-5z"/></svg>
      bluebellslimclinic.com
    </li>
  </ul>
</section>

</body>
</html>
```